Nectarine Point of Sale Cards for Grocery Retail Markets

We are looking to update our Nectarine point of sale card and price card. The cards will need to be 7" x 11" with a .125 bleed - one sided. See attached for the old versions. We would like this to use photos that look like true Washington State Peaches. Here are the bullet points we would like to use: - New Crop!- Tree Ripened- Excellent FlavorNOTE: The price card just needs to have a space where a retailer can write in the sale price of the item. See attachment with the white box.

Target Market(s)

Retail market shoppers

Requirements
Must have
• Pictures of Nectarines Only

```html
<!DOCTYPE html>
<html lang="en">
<head>
<meta charset="utf-8">
<title>Nectarine Point of Sale Cards</title>
<link href="https://fonts.googleapis.com/css2?family=Montserrat:wght@500;700;800&family=Source+Sans+3:wght@600;700&family=Great+Vibes&display=swap" rel="stylesheet">
<style>
  :root {
    --stage: #555555;
    --label: #e8ebb8;
    --green-dark: #2c6530;
    --green: #3a7c3c;
    --green-tick: #4aa14a;
    --text-green: #24552a;
    --white: #ffffff;
    --strip: #f1f1f1;
  }
  * { margin: 0; padding: 0; box-sizing: border-box; }
  html, body { width: 687px; height: 1200px; overflow: hidden; }
  body { background: var(--stage); position: relative; font-family: "Source Sans 3", sans-serif; }

  .sample-label {
    position: absolute; left: 0; width: 687px; text-align: center;
    font-family: "Source Sans 3", sans-serif; font-weight: 600;
    color: var(--label); font-size: 20px; letter-spacing: 0.3px;
  }
  .sample-label--one { top: 364px; }
  .sample-label--two { top: 740px; }
  .caption { top: 1131px; font-size: 21px; }

  .pos-card {
    position: absolute; left: 97px; width: 494px; height: 316px;
    overflow: hidden; background: var(--white);
  }
  .pos-card--one { top: 399px; }
  .pos-card--two { top: 780px; }

  .produce-photo {
    position: absolute; left: 0; top: 0; width: 494px; height: 258px;
    background:
      radial-gradient(ellipse 210px 120px at 160px 190px, #e07a4a 0%, #ea9a68 45%, rgba(236,180,130,0) 100%),
      radial-gradient(ellipse 260px 160px at 400px 60px, #e4efc2 0%, rgba(228,239,194,0) 100%),
      linear-gradient(180deg, #dfe9c9 0%, #eef2df 55%, #c9b39a 85%, #a98d72 100%);
  }

  .bottom-strip {
    position: absolute; left: 0; top: 258px; width: 494px; height: 58px;
    background: var(--strip);
  }

  .header-wave { position: absolute; left: 0; top: 0; }
  .header-text { position: absolute; color: var(--white); font-family: "Montserrat", sans-serif; }
  .header-text__state { left: 19px; top: 12px; font-size: 18px; font-weight: 500; letter-spacing: 0.2px; }
  .header-text__fruit { left: 18px; top: 30px; font-size: 31px; font-weight: 800; letter-spacing: -0.5px; }

  .header-band {
    position: absolute; left: 0; top: 0; width: 494px; height: 51px;
    background: linear-gradient(180deg, var(--green) 0%, var(--green-dark) 100%);
    color: var(--white); font-family: "Montserrat", sans-serif; font-weight: 800;
    font-size: 25px; line-height: 51px; text-align: center; letter-spacing: -0.3px;
  }

  .slogan {
    position: absolute; font-family: "Great Vibes", cursive; color: var(--green-dark);
    text-shadow: 0 0 2px #ffffff, 0 0 4px #ffffff; line-height: 1;
  }
  .slogan--stacked-top { left: 344px; top: 26px; font-size: 34px; }
  .slogan--stacked-main { left: 272px; top: 54px; font-size: 58px; }
  .slogan--wide { left: 0; width: 494px; text-align: center; top: 58px; font-size: 58px; }

  .benefits { position: absolute; left: 313px; top: 135px; list-style: none; }
  .benefits li {
    display: flex; align-items: center; height: 25px;
    font-weight: 700; font-size: 17px; color: var(--text-green);
  }
  .benefits svg { margin-right: 11px; flex: none; }

  .price-tag {
    position: absolute; left: 280px; top: 229px; width: 196px; height: 74px;
    background: var(--green-dark); border-radius: 12px;
  }
  .price-tag__label {
    position: absolute; left: 10px; top: 19px; color: var(--white);
    font-family: "Montserrat", sans-serif; font-weight: 700; font-size: 17px; line-height: 18px;
  }
  .price-tag__write-in {
    position: absolute; left: 76px; top: 3px; width: 117px; height: 68px;
    background: var(--white); border-radius: 12px;
  }

  .grower-mark { position: absolute; left: 19px; top: 266px; display: flex; align-items: center; }
  .grower-mark__dot { width: 40px; height: 40px; border-radius: 50%; background: #d9613a; margin-right: 9px; }
  .grower-mark__name { color: var(--green-dark); font-weight: 700; font-size: 11px; line-height: 11px; }
</style>
</head>
<body>

  <p class="sample-label sample-label--one">SAMPLE 1</p>

  <section class="pos-card pos-card--one">
    <div class="produce-photo" role="img" aria-label="Photo of ripe nectarines, one halved, with leaves on a wooden table before a soft green orchard background"></div>
    <div class="bottom-strip"></div>
    <svg class="header-wave" width="494" height="100" viewBox="0 0 494 100" aria-hidden="true">
      <path d="M0 0 H494 V24 C420 0 330 20 250 60 C170 98 70 96 0 76 Z" fill="#c8dcb0" opacity="0.7"/>
      <path d="M0 0 H494 V16 C420 -4 330 14 250 52 C170 90 70 88 0 68 Z" fill="#2f6b34"/>
    </svg>
    <p class="header-text header-text__state">WASHINGTON STATE</p>
    <p class="header-text header-text__fruit">NECTARINES</p>
    <p class="slogan slogan--stacked-top">Taste The</p>
    <p class="slogan slogan--stacked-main">Difference!</p>
    <ul class="benefits">
      <li><svg width="13" height="13" viewBox="0 0 13 13"><rect x="0.75" y="2.75" width="9.5" height="9.5" fill="none" stroke="#4aa14a" stroke-width="1.5"/><path d="M3 7 L5.5 9.5 L12 1.5" fill="none" stroke="#4aa14a" stroke-width="1.8"/></svg>New Crop!</li>
      <li><svg width="13" height="13" viewBox="0 0 13 13"><rect x="0.75" y="2.75" width="9.5" height="9.5" fill="none" stroke="#4aa14a" stroke-width="1.5"/><path d="M3 7 L5.5 9.5 L12 1.5" fill="none" stroke="#4aa14a" stroke-width="1.8"/></svg>Tree Ripened</li>
      <li><svg width="13" height="13" viewBox="0 0 13 13"><rect x="0.75" y="2.75" width="9.5" height="9.5" fill="none" stroke="#4aa14a" stroke-width="1.5"/><path d="M3 7 L5.5 9.5 L12 1.5" fill="none" stroke="#4aa14a" stroke-width="1.8"/></svg>Excellent Flavor</li>
    </ul>
    <div class="grower-mark">
      <span class="grower-mark__dot"></span>
      <p class="grower-mark__name">Cascade Orchard<br>Growers Council</p>
    </div>
    <div class="price-tag">
      <p class="price-tag__label">PRICE<br>ONLY</p>
      <div class="price-tag__write-in"></div>
    </div>
  </section>

  <p class="sample-label sample-label--two">SAMPLE 2</p>

  <section class="pos-card pos-card--two">
    <div class="produce-photo" role="img" aria-label="Photo of ripe nectarines, one halved, with leaves on a wooden table before a soft green orchard background"></div>
    <div class="bottom-strip"></div>
    <h2 class="header-band">WASHINGTON STATE NECTARINES</h2>
    <p class="slogan slogan--wide">Taste The Difference!</p>
    <ul class="benefits">
      <li><svg width="13" height="13" viewBox="0 0 13 13"><rect x="0.75" y="2.75" width="9.5" height="9.5" fill="none" stroke="#4aa14a" stroke-width="1.5"/><path d="M3 7 L5.5 9.5 L12 1.5" fill="none" stroke="#4aa14a" stroke-width="1.8"/></svg>New Crop!</li>
      <li><svg width="13" height="13" viewBox="0 0 13 13"><rect x="0.75" y="2.75" width="9.5" height="9.5" fill="none" stroke="#4aa14a" stroke-width="1.5"/><path d="M3 7 L5.5 9.5 L12 1.5" fill="none" stroke="#4aa14a" stroke-width="1.8"/></svg>Tree Ripened</li>
      <li><svg width="13" height="13" viewBox="0 0 13 13"><rect x="0.75" y="2.75" width="9.5" height="9.5" fill="none" stroke="#4aa14a" stroke-width="1.5"/><path d="M3 7 L5.5 9.5 L12 1.5" fill="none" stroke="#4aa14a" stroke-width="1.8"/></svg>Excellent Flavor</li>
    </ul>
    <div class="grower-mark">
      <span class="grower-mark__dot"></span>
      <p class="grower-mark__name">Cascade Orchard<br>Growers Council</p>
    </div>
    <div class="price-tag">
      <p class="price-tag__label">PRICE<br>ONLY</p>
      <div class="price-tag__write-in"></div>
    </div>
  </section>

  <p class="sample-label caption">NECTARINE POINT OF SALE CARDS FOR GROCERY</p>

</body>
</html>
```